Website for Swedish wellness company "Heartmeadow"

We need a website for our Swedish wellness company. The name is "Heartmeadow" . The company is all about sustainablility for our body, soul and planet. We work with coaching, yoga, massage, healthy food, retreats(sports, excercise, sufing), healing and inspirational talks. We are convinced that personal sustainability and a strong spiritual connection to yourself will lead to planetary sustainability. Our customers are both companies and consumers from all over the world. The final design should be clean/simple and you should get a feeling of community, happiness, warmth, connection,, joy, spirituality but still a professional touch.Just got a logo from Pixel Harbor and are very happy with it;-)
Updates

Sorry I was too enthusiastic posting this project. Of course I will give you some text as well för the different pages! I will see to that it is finished by friday so if you want to wait with your submissions please do! Best regards Maria

Target Market(s)

Businesses and consumers

Industry/Entity Type

Health And Wellness

Number of Pages Required

5+ page

Font styles to use
Sans Serif

Colors
33a6d7
00a990
b7a5cd

Requirements
Must have
• Idea about pages:
• I am not sure how many pages I get for the price, but 5 would be nice to start with.
• Not sure what write ups is;-)
• But title of the pages could be:
• Landing page
• About us
• Services
• Retreats
• Contact us
Nice to have
• A clean and professional website but with some heart and soul in it. Because we Would love colours that harmonize with our logo, but other ideas are welcome!

```html
<!DOCTYPE html>
<html lang="en">
<head>
<meta charset="utf-8">
<title>Heartmeadow — Wellness Website</title>
<link href="https://fonts.googleapis.com/css2?family=Signika:wght@400;600&family=Open+Sans:wght@400;600;700&display=swap" rel="stylesheet">
<style>
:root{
  --blue:#33a6d7;
  --teal:#00a990;
  --slate:#8c9a98;
  --ink:#2c4a55;
  --muted:#8a969a;
  --band:#ececec;
  --white:#ffffff;
  --stage:#e4e4e4;
}
*{box-sizing:border-box;margin:0;padding:0}
html,body{width:1200px;height:1200px;overflow:hidden;background:var(--stage)}
body{font-family:"Open Sans",sans-serif;color:var(--ink)}
.page{position:absolute;left:404px;top:0;width:916px;height:2808px;background:var(--white);transform:scale(.4274);transform-origin:0 0;box-shadow:0 0 30px rgba(0,0,0,.25);overflow:hidden}
.abs{position:absolute}
.photo{position:absolute}
.hero-photo{left:0;top:0;width:916px;height:488px;
  background:
    radial-gradient(ellipse 150px 260px at 150px 300px,rgba(246,244,238,.95),rgba(246,244,238,0) 75%),
    radial-gradient(ellipse 260px 110px at 300px 210px,rgba(52,120,104,.85),rgba(52,120,104,0) 80%),
    radial-gradient(ellipse 320px 80px at 640px 250px,rgba(132,176,176,.55),rgba(132,176,176,0) 80%),
    linear-gradient(180deg,#e4f1f2 0%,#cfe6e8 34%,#a9cfcf 48%,#bcdcdd 62%,#d6eaea 82%,#e9f2f1 100%)}
.hero-fade{left:0;top:0;width:916px;height:488px;background:linear-gradient(90deg,rgba(255,255,255,0) 45%,rgba(255,255,255,.35) 100%)}
.logo{left:160px;top:20px;display:flex;align-items:center;gap:10px}
.logo-dot{width:30px;height:30px;border-radius:50%;background:var(--blue)}
.logo-name{font-weight:600;font-size:16px;color:var(--ink);letter-spacing:.5px}
.nav{right:170px;top:34px;display:flex;gap:20px;font-size:10px;color:var(--muted)}
.nav .active{color:var(--blue);font-weight:600}
.hero-title{right:170px;top:216px;font-family:"Signika",sans-serif;font-weight:400;font-size:34px;color:var(--teal);text-align:right}
.hero-text{right:170px;top:262px;width:290px;font-size:9px;line-height:1.4;text-align:right;color:var(--ink)}
.btn{display:inline-block;background:var(--blue);color:var(--white);font-size:7px;font-weight:700;padding:5px 12px;letter-spacing:.5px}
.hero-btn{right:170px;top:314px}
.info{top:424px;width:191px;height:126px;color:var(--white);text-align:center;font-size:7px;line-height:1.5;padding-top:22px}
.info h4{font-size:8px;font-weight:600;letter-spacing:.5px;margin:8px 0 6px}
.info svg{width:18px;height:18px}
.heading{left:0;width:916px;text-align:center;font-size:17px;font-weight:400;color:var(--ink)}
.heading.caps{text-transform:uppercase;letter-spacing:1px}
.divider{left:398px;width:120px;height:14px}
.about-photo{left:172px;top:664px;width:328px;height:174px;
  background:
    radial-gradient(ellipse 80px 70px at 164px 80px,rgba(240,220,250,.9),rgba(240,220,250,0) 80%),
    radial-gradient(ellipse 140px 40px at 164px 150px,rgba(236,170,110,.8),rgba(236,170,110,0) 80%),
    linear-gradient(180deg,#3d5f97,#6e78b8 40%,#8a8fb8 65%,#3b5a66)}
.about-text{left:514px;top:666px;width:232px;font-size:8px;line-height:1.5;color:var(--muted)}
.about-text h5{font-size:9px;color:var(--ink);font-weight:600;margin-bottom:6px}
.more{font-size:7px;color:var(--muted);text-align:right;margin-top:10px}
.band{left:0;width:916px;background:var(--band)}
.svc{top:984px;width:132px;height:192px;background:var(--white);text-align:center;padding-top:16px}
.svc .thumb{width:70px;height:70px;border-radius:50%;margin:0 auto 10px}
.svc h6{font-size:8px;color:var(--blue);font-weight:600;margin-bottom:6px}
.svc p{font-size:6.5px;line-height:1.5;color:var(--muted);padding:0 12px}
.svc .btn{margin-top:10px;font-size:5.5px;padding:3px 9px}
.blog-img{top:1338px;width:136px;height:96px}
.blog-text{top:1340px;width:140px;font-size:6.5px;line-height:1.5;color:var(--muted)}
.blog-text h6{font-size:7.5px;color:var(--ink);font-weight:600;margin-bottom:6px}
.cta-photo{left:0;top:1484px;width:916px;height:170px;
  background:
    radial-gradient(ellipse 260px 90px at 460px 40px,rgba(214,180,130,.55),rgba(214,180,130,0) 80%),
    linear-gradient(180deg,#6d6152 0%,#8a7b66 40%,#5b4f42 70%,#3f372e 100%)}
.cta-text{left:0;top:1526px;width:916px;text-align:center;color:var(--white);font-size:13px;line-height:1.6}
.cta-text strong{font-size:16px;font-weight:600}
.team{top:1814px;width:182px;height:192px}
.team .photo{left:0;top:0;width:182px;height:150px}
.team-label{position:absolute;left:0;bottom:0;width:182px;height:42px;background:var(--blue);color:var(--white);text-align:center;font-size:9px;font-weight:600;padding-top:8px}
.team-label small{display:block;font-size:6.5px;font-weight:400}
.team-feature{background:var(--blue);color:var(--white);text-align:center;padding:22px 14px;font-size:6.5px;line-height:1.6}
.team-feature h6{font-size:10px;font-weight:600}
.dots{display:flex;gap:5px;justify-content:center}
.dots span{width:6px;height:6px;border-radius:50%;border:1px solid var(--blue)}
.dots .on{background:var(--blue)}
.quote-photo{left:438px;top:2186px;width:40px;height:40px;border-radius:50%;background:linear-gradient(#c9b3a4,#7e6a60)}
.quote{left:220px;top:2240px;width:476px;text-align:center;font-size:7px;line-height:1.6;color:var(--muted)}
.stat{top:2376px;width:140px;text-align:center;font-size:11px;color:var(--blue)}
.stat svg{display:block;margin:0 auto 6px;width:18px;height:18px}
.contact h5,.quick h5{font-size:11px;letter-spacing:1px;font-weight:600;color:var(--ink)}
.contact-lines{font-size:7px;line-height:2.2;color:var(--ink)}
.social{display:flex;gap:5px;margin-top:6px}
.social span{width:11px;height:11px;border-radius:50%;background:var(--blue)}
.social span:nth-child(2){background:#e05a4d}
.social span:nth-child(4){background:var(--teal)}
.footer{left:0;top:2606px;width:916px;height:202px;background:var(--teal)}
.footer h6{font-size:9px;color:var(--white);letter-spacing:1px;font-weight:600}
.footer ul{list-style:none;font-size:6.5px;color:var(--white);line-height:1.9;margin-top:8px}
.map{left:304px;top:2648px;width:200px;height:104px;background:linear-gradient(135deg,#eef1f3,#c8d0d6)}
.copy{position:absolute;left:172px;top:172px;width:572px;text-align:center;font-size:6.5px;color:var(--white);border-top:1px solid rgba(255,255,255,.4);padding-top:8px}
.form{left:576px;top:2500px;width:170px;height:250px;background:var(--white);border:1px solid #d5dcdc;padding:12px}
.field{height:13px;border:1px solid #cfd6d6;margin-bottom:8px;font-size:5.5px;color:var(--muted);padding:2px 4px}
.field.tall{height:38px}
.form p{font-size:5.5px;color:var(--muted);line-height:1.5;margin:4px 0 8px}
</style>
</head>
<body>
<main class="page">

  <!-- Hero -->
  <div class="photo hero-photo" role="img" aria-label="Woman meditating on a lakeside pier with misty mountains"></div>
  <div class="abs hero-fade"></div>
  <div class="abs logo"><span class="logo-dot"></span><span class="logo-name">HEARTMEADOW</span></div>
  <nav class="abs nav"><span class="active">Home</span><span>About us</span><span>Services</span><span>Retreats</span><span>Contact us</span><span>⌕</span></nav>
  <h1 class="abs hero-title">Power Of Nature</h1>
  <p class="abs hero-text">Find calm in body and soul with our retreats, coaching and daily practice, guided by people who care about you and the planet we share.</p>
  <span class="abs btn hero-btn">VIEW MORE</span>

  <div class="abs info" style="left:172px;background:var(--blue)">
    <svg viewBox="0 0 20 20" fill="none" stroke="#fff" stroke-width="1.4"><circle cx="10" cy="11" r="7"/><path d="M10 7v4l3 2M4 3l3 2M16 3l-3 2"/></svg>
    <h4>OPEN HOURS</h4>Monday-Friday: 08:00-20:00<br>Saturday: 09:00-18:00<br>Sunday: 10:00-16:00
  </div>
  <div class="abs info" style="left:363px;background:var(--slate)">
    <svg viewBox="0 0 20 20" fill="none" stroke="#fff" stroke-width="1.4"><rect x="4" y="2" width="11" height="15" rx="1"/><path d="M7 6h5M7 9h5M7 12h3"/><circle cx="15" cy="15" r="3"/></svg>
    <h4>APPOINTMENTS</h4>Call us to book your appointment at<br>046-555-0182<br>or sign up online.
  </div>
  <div class="abs info" style="left:554px;background:var(--teal)">
    <svg viewBox="0 0 20 20" fill="none" stroke="#fff" stroke-width="1.4"><rect x="3" y="3" width="14" height="14" rx="1"/><path d="M6 13l3-4 3 3 2-2"/></svg>
    <h4>NEWS &amp; MEDIA</h4>Read our latest stories and events<br>from the community and our<br>retreats around the world.
  </div>

  <!-- About -->
  <h2 class="abs heading" style="top:594px">About Us</h2>
  <svg class="abs divider" style="top:620px" viewBox="0 0 120 14"><path d="M0 7h50M70 7h50" stroke="#b8c2c4"/><circle cx="60" cy="7" r="5" fill="none" stroke="#b8c2c4"/></svg>
  <div class="photo about-photo" role="img" aria-label="Meditating figure with glowing chakra colours"></div>
  <div class="abs about-text">
    <h5>An Introduction</h5>
    <p>We believe personal wellbeing grows into care for the planet. Our team offers yoga, massage and coaching for people and companies.</p><br>
    <p>Every session is built on warmth, joy and connection, so you leave feeling lighter and closer to yourself and others.</p><br>
    <p>Join us at home in Sweden or at one of our retreats by the sea and mountains.</p>
    <p class="more">READ MORE →</p>
  </div>

  <!-- Services -->
  <div class="abs band" style="top:886px;height:340px"></div>
  <h2 class="abs heading" style="top:928px">Services We Provide</h2>
  <svg class="abs divider" style="top:954px" viewBox="0 0 120 14"><path d="M0 7h50M70 7h50" stroke="#b8c2c4"/><circle cx="60" cy="7" r="5" fill="none" stroke="#b8c2c4"/></svg>
  <div class="abs svc" style="left:172px"><div class="thumb" role="img" aria-label="Yoga class" style="background:radial-gradient(circle at 45% 40%,#f1d9d0,#9fb4cf 60%,#5a7aa6)"></div><h6>Yoga</h6><p>Gentle flows for all levels to build strength and calm.</p><span class="btn">LEARN MORE</span></div>
  <div class="abs svc" style="left:318px"><div class="thumb" role="img" aria-label="Massage session" style="background:radial-gradient(circle at 40% 45%,#d99a72,#8c5034 55%,#3a2014)"></div><h6>Massage Spa</h6><p>Relaxing treatments that release tension and restore.</p><span class="btn">LEARN MORE</span></div>
  <div class="abs svc" style="left:464px"><div class="thumb" role="img" aria-label="Healthy food" style="background:radial-gradient(circle at 50% 40%,#f7c24a,#e3802c 55%,#9d3a22)"></div><h6>Healthy Food</h6><p>Fresh seasonal meals made to nourish body and soul.</p><span class="btn">LEARN MORE</span></div>
  <div class="abs svc" style="left:612px"><div class="thumb" role="img" aria-label="Retreat in nature" style="background:radial-gradient(circle at 50% 40%,#cfe8c0,#6fb07a 55%,#2c6e46)"></div><h6>Retreats</h6><p>Surf, sport and rest in beautiful places worldwide.</p><span class="btn">LEARN MORE</span></div>

  <!-- Blog -->
  <h2 class="abs heading caps" style="top:1268px">Latest From The Blog</h2>
  <svg class="abs divider" style="top:1294px" viewBox="0 0 120 14"><path d="M0 7h50M70 7h50" stroke="#b8c2c4"/><circle cx="60" cy="7" r="5" fill="none" stroke="#b8c2c4"/></svg>
  <div class="photo blog-img" role="img" aria-label="Spa stones, towels and candle" style="left:172px;background:radial-gradient(ellipse 40px 30px at 100px 60px,rgba(255,190,90,.8),rgba(255,190,90,0)),linear-gradient(180deg,#6b4326,#3a2414)"></div>
  <div class="abs blog-text" style="left:322px"><h6>Wellness and beauty salon</h6><p>Simple rituals for a calmer week, from breathing to rest and warm baths at home.</p><p class="more">READ MORE →</p></div>
  <div class="photo blog-img" role="img" aria-label="Stones and red flower" style="left:466px;background:radial-gradient(ellipse 40px 30px at 110px 70px,rgba(205,40,40,.85),rgba(205,40,40,0)),linear-gradient(180deg,#9fc3dc,#e9eef2 70%,#f5f5f5)"></div>
  <div class="abs blog-text" style="left:616px"><h6>The best body cures</h6><p>Our coaches share their favourite ways to stay strong, rested and happy all year.</p><p class="more">READ MORE →</p></div>

  <!-- Call to action -->
  <div class="photo cta-photo" role="img" aria-label="People exercising on a beach at sunset"></div>
  <div class="abs cta-text">Want to join world's best wellness program<br><strong>call us: 046-555-0182</strong><br><span class="btn">CONTACT US</span></div>

  <!-- Team -->
  <div class="abs band" style="top:1702px;height:374px"></div>
  <h2 class="abs heading caps" style="top:1746px">Meet Our Team</h2>
  <svg class="abs divider" style="top:1772px" viewBox="0 0 120 14"><path d="M0 7h50M70 7h50" stroke="#b8c2c4"/><circle cx="60" cy="7" r="5" fill="none" stroke="#b8c2c4"/></svg>
  <div class="abs team" style="left:172px"><div class="photo" role="img" aria-label="Portrait of team member" style="background:linear-gradient(180deg,#e6eaec,#d9c6ae 60%,#c7b39a)"></div><div class="team-label">Linnea Berg<small>(Power Yoga Expert)</small></div></div>
  <div class="abs team team-feature" style="left:368px"><h6>Sofia Lund</h6><small>(Wellness Trainer)</small><p style="margin-top:14px">Sofia guides our retreats and helps every guest find a pace that feels good, with care, humour and lots of energy.</p><div class="social" style="justify-content:center;margin-top:12px"><span style="background:#fff"></span><span style="background:#fff"></span><span style="background:#fff"></span></div></div>
  <div class="abs team" style="left:562px"><div class="photo" role="img" aria-label="Portrait of team member" style="background:linear-gradient(180deg,#ececec,#c98a5e 55%,#8e4e2e)"></div><div class="team-label">Erik Holm<small>(Spa Manager)</small></div></div>
  <div class="abs dots" style="left:0;width:916px;top:2022px"><span></span><span class="on"></span><span></span></div>

  <!-- Testimonials -->
  <h2 class="abs heading" style="top:2120px">Testimonials</h2>
  <svg class="abs divider" style="top:2146px" viewBox="0 0 120 14"><path d="M0 7h50M70 7h50" stroke="#b8c2c4"/><circle cx="60" cy="7" r="5" fill="none" stroke="#b8c2c4"/></svg>
  <div class="abs quote-photo" role="img" aria-label="Customer portrait"></div>
  <p class="abs quote">A week with this team changed how I look after myself. The yoga mornings, the food and the people made me feel at home, and I came back with more energy, more joy and a real wish to live lighter on the planet.<br><br><span style="color:var(--ink)">Anna Ek</span></p>
  <div class="abs dots" style="left:0;width:916px;top:2304px"><span></span><span class="on"></span><span></span></div>

  <!-- Stats -->
  <div class="abs band" style="top:2356px;height:82px"></div>
  <div class="abs stat" style="left:172px"><svg viewBox="0 0 20 20"><circle cx="10" cy="10" r="8" fill="var(--blue)"/></svg>50+ Countries</div>
  <div class="abs stat" style="left:312px"><svg viewBox="0 0 20 20" fill="none" stroke="var(--blue)" stroke-width="1.6"><rect x="5" y="2" width="10" height="16"/><path d="M8 6h4M8 10h4M8 14h4"/></svg>200+ Centers</div>
  <div class="abs stat" style="left:452px"><svg viewBox="0 0 20 20"><circle cx="10" cy="10" r="8" fill="var(--blue)"/><circle cx="10" cy="8" r="3" fill="#fff"/></svg>900+ Experts</div>
  <div class="abs stat" style="left:596px"><svg viewBox="0 0 20 20"><circle cx="10" cy="10" r="8" fill="var(--teal)"/></svg>30000+ Trainees</div>

  <!-- Contact -->
  <div class="abs contact" style="left:172px;top:2474px">
    <h5>CONTACT INFORMATION</h5>
    <div style="display:flex;gap:46px;margin-top:6px">
      <div class="contact-lines">⌖ 12 Ängsvägen Lund 223 50<br>✆ 046-555-0182<br>✉ info@heartmeadow.se</div>
      <div class="contact-lines">We Are Social :<div class="social"><span></span><span></span><span></span><span></span><span></span></div></div>
    </div>
  </div>
  <div class="abs quick" style="left:576px;top:2474px"><h5>QUICK APPOINTMENTS</h5></div>

  <!-- Footer -->
  <div class="abs footer">
    <div class="abs" style="left:172px;top:20px"><h6>SERVICES</h6><ul><li>• Coaching</li><li>• Yoga</li><li>• Massage</li><li>• Healthy Food</li><li>• Retreats</li><li>• Healing</li><li>• Inspirational Talks</li></ul></div>
    <div class="abs" style="left:304px;top:20px"><h6>LOCATION</h6></div>
    <p class="copy">Copyright 2024 Heartmeadow. All Rights Reserved</p>
  </div>
  <div class="photo map" role="img" aria-label="Map showing the studio location"></div>
  <div class="abs form">
    <div class="field">Name *</div><div class="field">Email *</div><div class="field">Phone *</div><div class="field">Service ⌄</div><div class="field tall">Message *</div>
    <p>☐ I agree that Heartmeadow may contact me about my booking.</p>
    <span class="btn">SUBMIT</span>
  </div>
</main>
</body>
</html>
```